Business card design needed

We are a not for profit organisation that assists the spinal cord injured community (paraplegics and quadriplegics) with funding for new equipment, ie wheelchairs, commodes etc as well as psychology services, supporting the injured and their families.

Industry/Entity Type

Business

Contact Information for Business Card

Daniel Marsh Foundation (logo)
"Helping the Spinal Community"
Clara Denbigh - Executive Officer
PO Box 614 Kelverton Vic 3192
Ph: 03 9471 2258 www.danielmarshfoundation.com
Email: danielmarshfoundation@mailvane.com

Requirements
Must have
• perhaps a drawing or picture of a wheelchair...ultra modern looking.

```html
<!DOCTYPE html>
<html lang="en">
<head>
<meta charset="utf-8">
<title>Daniel Marsh Foundation – Business Card</title>
<link href="https://fonts.googleapis.com/css2?family=Noto+Serif:wght@400;700&display=swap" rel="stylesheet">
<style>
  :root {
    --backdrop: #3a3a3c;
    --orange: #eea20e;
    --orange-light: #f8be3a;
    --orange-deep: #d98a05;
    --paper: #ffffff;
    --paper-shade: #ececec;
    --ink: #4a4a4a;
    --white: #ffffff;
  }
  * { box-sizing: border-box; margin: 0; padding: 0; }
  html, body {
    width: 1200px; height: 874px; overflow: hidden;
    background: var(--backdrop);
    font-family: "Noto Serif", Georgia, serif;
  }
  .canvas { position: relative; width: 1200px; height: 874px; }

  .card {
    position: absolute;
    border-radius: 3px;
    box-shadow: 0 10px 28px rgba(0,0,0,.45);
    overflow: hidden;
  }

  /* Front */
  .card-front {
    left: 110px; top: 160px; width: 340px; height: 554px;
  }
  .front-rays {
    position: absolute; inset: 0;
    background: radial-gradient(circle at 55% 45%, var(--orange-light) 0%, var(--orange) 55%, var(--orange-deep) 100%);
  }
  .front-mark {
    position: absolute; left: 50%; top: 45%;
    transform: translate(-50%, -50%);
    display: flex; flex-direction: column; align-items: center; gap: 14px;
  }
  .mark-dot {
    width: 60px; height: 60px; border-radius: 50%;
    background: var(--white);
  }
  .front-mark .mark-name {
    color: var(--white); font-weight: 700; font-size: 22px;
    text-align: center; line-height: 1.25;
  }

  /* Back */
  .card-back {
    left: 520px; top: 250px; width: 580px; height: 354px;
    background: linear-gradient(180deg, var(--paper) 0%, var(--paper) 60%, var(--paper-shade) 100%);
  }
  .back-band { position: absolute; left: 0; bottom: 0; width: 580px; height: 120px; }
  .back-mark {
    position: absolute; left: 40px; top: 92px; width: 170px;
    display: flex; flex-direction: column; align-items: center; gap: 10px;
  }
  .back-mark .mark-dot { background: var(--orange); width: 52px; height: 52px; }
  .back-mark .mark-name {
    color: var(--orange); font-weight: 700; font-size: 17px;
    text-align: center; line-height: 1.25;
  }
  .contact {
    position: absolute; right: 34px; top: 38px; width: 320px;
    text-align: right; color: var(--ink);
  }
  .contact-name { color: var(--orange); font-weight: 700; font-size: 25px; }
  .contact-role { color: var(--orange); font-size: 15px; margin-bottom: 16px; }
  .contact-line { font-size: 12px; line-height: 1.55; }
  .contact-gap { height: 14px; }
</style>
</head>
<body>
<main class="canvas">

  <section class="card card-front">
    <div class="front-rays" role="img" aria-label="Orange sunburst ray background"></div>
    <div class="front-mark">
      <span class="mark-dot"></span>
      <span class="mark-name">Daniel Marsh<br>Foundation</span>
    </div>
  </section>

  <section class="card card-back">
    <svg class="back-band" viewBox="0 0 580 120" preserveAspectRatio="none" aria-hidden="true">
      <defs>
        <linearGradient id="bandFill" x1="0" y1="0" x2="1" y2="0">
          <stop offset="0" stop-color="var(--orange-deep)"/>
          <stop offset="0.6" stop-color="var(--orange)"/>
          <stop offset="1" stop-color="var(--orange-light)"/>
        </linearGradient>
      </defs>
      <path d="M0 120 L0 95 C170 80 360 40 580 10 L580 120 Z" fill="url(#bandFill)"/>
      <path d="M0 95 C170 80 360 40 580 10" stroke="var(--orange-light)" stroke-width="3" fill="none"/>
    </svg>

    <div class="back-mark">
      <span class="mark-dot"></span>
      <span class="mark-name">Daniel Marsh<br>Foundation</span>
    </div>

    <div class="contact">
      <p class="contact-name">Clara Denbigh</p>
      <p class="contact-role">Executive Officer</p>
      <p class="contact-line">PO Box 614 Kelverton Vic 3192</p>
      <p class="contact-line">Ph. 03 9471 2258</p>
      <div class="contact-gap"></div>
      <p class="contact-line">Email: danielmarshfoundation@mailvane.com</p>
      <p class="contact-line">www.danielmarshfoundation.com</p>
    </div>
  </section>

</main>
</body>
</html>
```